Two Day Training Event includes a Dinner/Bowling Party at Pinhollow in Troy, MI

I would like a postcard to attract Insurance Agents to an KRV meeting calling it a summit or something like that. Just something to mail to insurance agents telling them about our upcoming event with over 20 carriers. An opportunity to certify face to face with MAPD carriers and see what 2020 has to offer. Prior to OEP OPen Enrollment and AEP Annual Election period we have a number of meetings. Carriers want to come especially if we can get a number of agents. We are going to go to Pinhollow a fun bowling alley for dinner, drinks and bowling to network and talk about the upcoming year.

Target Market(s)

Existing and new insurance agents

Industry/Entity Type

Insurance Broker

Contact Information for Business Card

Looking for a new card design I sent my LOGO and can upload my existing card.

Font styles to use
Serif

Colors

Designer to choose colors to be used in the design.

Requirements
Must have
• Dates Sept 16 and 17th
• location Larkfield Conference Hall in Troy MI
• times
Nice to have
• It would be nice to see a fun design.

```html
<!DOCTYPE html>
<html lang="en">
<head>
<meta charset="utf-8">
<title>KRV Two Day Training Event Flyer</title>
<link rel="stylesheet" href="https://fonts.googleapis.com/css2?family=Arimo:wght@400;700&family=Roboto:wght@700;900&display=swap">
<style>
  :root {
    --page-bg: #e6f5f3;
    --flyer-bg: #071a26;
    --flyer-glow: #0d2a36;
    --gold: #f2c230;
    --gold-light: #f7d662;
    --frame-a: #b8891e;
    --frame-b: #ffe58a;
    --text-font: "Arimo", Arial, sans-serif;
    --head-font: "Roboto", Arial, sans-serif;
  }
  * { margin: 0; padding: 0; box-sizing: border-box; }
  html, body { width: 1200px; height: 800px; overflow: hidden; }
  body { background: var(--page-bg); position: relative; font-family: var(--text-font); }

  .flyer {
    position: absolute; left: 337px; top: 28px;
    width: 526px; height: 744px;
    background: var(--flyer-bg);
    color: var(--gold);
  }
  .flyer__confetti {
    position: absolute; inset: 0;
    background: radial-gradient(ellipse at 50% 45%, var(--flyer-glow), var(--flyer-bg) 75%);
  }
  .flyer__frame {
    position: absolute; left: 16px; top: 16px; right: 16px; bottom: 16px;
    border: 4px solid var(--frame-a);
    border-image: linear-gradient(135deg, var(--frame-a), var(--frame-b), var(--frame-a), var(--frame-b)) 1;
  }

  .line {
    position: absolute; left: 0; right: 0;
    text-align: center; transform: translateY(-50%);
    white-space: nowrap;
  }
  .brand {
    top: 74px; font-family: var(--text-font); font-weight: 700;
    font-size: 44px; letter-spacing: 2px; color: var(--gold);
    display: flex; justify-content: center; align-items: center; gap: 10px;
  }
  .brand__mark { width: 14px; height: 14px; background: var(--gold); display: inline-block; }
  .invite { top: 134px; font-family: var(--head-font); font-weight: 700; font-size: 20px; color: var(--gold-light); }
  .heading {
    font-family: var(--head-font); font-weight: 700; font-size: 22px;
    color: var(--gold-light); text-decoration: underline; text-underline-offset: 4px;
  }
  .event-title { top: 183px; }
  .feature { font-size: 19px; letter-spacing: 0.3px; }
  .feature--one { top: 222px; }
  .feature--two { top: 258px; }
  .speakers-title { top: 306px; }
  .speaker-name { font-size: 20px; letter-spacing: 1.5px; }
  .speaker-role { font-size: 12px; color: var(--gold-light); letter-spacing: 0.3px; }
  .speaker-one { top: 341px; }
  .speaker-one-role { top: 362px; }
  .speaker-two { top: 393px; }
  .speaker-two-role { top: 414px; }
  .and { top: 469px; font-family: var(--head-font); font-weight: 700; font-size: 25px; color: var(--gold-light); }
  .party { top: 517px; font-family: var(--head-font); font-weight: 900; font-size: 27px; letter-spacing: 3.5px; color: var(--gold-light); }

  .info { position: absolute; width: 250px; top: 576px; text-align: center; }
  .info--venue { left: 7px; }
  .info--contact { left: 257px; }
  .info .heading { display: block; margin-bottom: 8px; font-size: 20px; }
  .info p { font-size: 14px; line-height: 17px; letter-spacing: 0.3px; }
  .info .strong { font-weight: 700; font-size: 14px; letter-spacing: 0.6px; margin-top: 5px; line-height: 18px; }
</style>
</head>
<body>
  <main class="flyer">
    <div class="flyer__confetti" role="img" aria-label="Scattered confetti pieces and curled streamers in teal, purple and green"></div>
    <div class="flyer__frame"></div>

    <div class="line brand"><span class="brand__mark"></span>KRV</div>
    <div class="line invite">Inviting you to come and join</div>

    <h1 class="line heading event-title">2 Days Training Event</h1>
    <p class="line feature feature--one">Major medical &amp; senior products</p>
    <p class="line feature feature--two">Face to face with MAPD carriers</p>

    <h2 class="line heading speakers-title">Speakers</h2>
    <p class="line speaker-name speaker-one">Owen Malloy</p>
    <p class="line speaker-role speaker-one-role">(Health and Medicare Specialist)</p>
    <p class="line speaker-name speaker-two">Reid Hollins</p>
    <p class="line speaker-role speaker-two-role">(Health and Medicare Area Manager)</p>

    <p class="line and">AND</p>
    <p class="line party">A DINNER/BOWLING PARTY</p>

    <section class="info info--venue">
      <h3 class="heading">Venue &amp; Time</h3>
      <p>Larkfield Conference<br>Hall,<br>Troy MI</p>
      <p class="strong">Sept 16 and 17th<br>03:00 PM - 08:30 PM</p>
    </section>

    <section class="info info--contact">
      <h3 class="heading">Contact Us</h3>
      <p>418 Alder Park Dr. Suite 120<br>Troy, MI</p>
      <p class="strong">(555) 014-2297</p>
      <p>rhollins@krvmail.com</p>
    </section>
  </main>
</body>
</html>
```